Business Executives Need Book Cover Design

We need a custom book cover instead of the boring stock cover that was available on PressLoom.
The current cover can be seen at:
http://www.shelvaro.example/Ledger-Metrics-Leaders-Directors-hoped/dp/7302846615
We like this cover in general (the colors, general layout and picture), but you can see it needs help with the spacing of the Authors names and general design. Also, since it is stock, someone else could have the same cover. It is for business executives so it should be classy. It should communicate that it is for executives. The book is only available in soft cover.

Target Market(s)

Business School students, business executives

Industry/Entity Type

Business

Requirements
Must have
• book name and authors names.

```html
<!DOCTYPE html>
<html lang="en">
<head>
<meta charset="utf-8">
<title>Ledger Metrics for Leaders &amp; Finance Directors — Book Cover</title>
<link href="https://fonts.googleapis.com/css2?family=Cabin:wght@400;500&display=swap" rel="stylesheet">
<style>
  :root {
    --ink: #000000;
    --paper: #ffffff;
    --spectrum-red: #9e2a1c;
    --spectrum-orange: #c9772a;
    --spectrum-yellow: #c9b83a;
    --spectrum-green: #3f8f55;
    --spectrum-blue: #2a6fae;
    --deep-blue: #163d6e;
    --steel: #6f7c88;
    --slate: #3e4650;
    --umber: #6a5e48;
  }
  html, body {
    margin: 0;
    padding: 0;
    width: 926px;
    height: 1200px;
    overflow: hidden;
    background: var(--paper);
  }
  .cover {
    position: relative;
    width: 926px;
    height: 1200px;
    overflow: hidden;
    font-family: "Cabin", "Gill Sans", sans-serif;
  }
  .cover-art {
    position: absolute;
    inset: 0;
    background:
      radial-gradient(ellipse 60% 30% at 55% 92%, rgba(60,70,80,0.75), rgba(60,70,80,0) 70%),
      radial-gradient(ellipse 45% 35% at 95% 100%, rgba(106,94,72,0.85), rgba(106,94,72,0) 70%),
      radial-gradient(ellipse 60% 45% at 80% 35%, rgba(30,90,160,0.8), rgba(30,90,160,0) 70%),
      radial-gradient(ellipse 40% 30% at 10% 95%, rgba(110,120,130,0.8), rgba(110,120,130,0) 70%),
      linear-gradient(112deg,
        var(--spectrum-red) 0%,
        var(--spectrum-orange) 10%,
        var(--spectrum-yellow) 22%,
        var(--spectrum-green) 33%,
        var(--spectrum-blue) 48%,
        var(--deep-blue) 66%,
        var(--steel) 84%,
        var(--slate) 100%);
  }
  .title-plate {
    position: absolute;
    left: 90px;
    top: 160px;
    width: 746px;
    height: 336px;
    box-sizing: border-box;
    background: var(--ink);
    border: 6px solid var(--paper);
    box-shadow: 0 0 0 3px var(--ink);
  }
  .title-plate::before {
    content: "";
    position: absolute;
    inset: 8px;
    border: 3px solid var(--paper);
  }
  .book-title {
    position: absolute;
    inset: 0;
    margin: 0;
    display: flex;
    flex-direction: column;
    justify-content: center;
    align-items: center;
    color: var(--paper);
    font-weight: 400;
    font-size: 72px;
    line-height: 74px;
    letter-spacing: 1.5px;
    text-align: center;
  }
  .author-band {
    position: absolute;
    left: 0;
    right: 0;
    top: 892px;
    height: 174px;
    border-top: 3px solid var(--paper);
    border-bottom: 3px solid var(--paper);
    box-sizing: border-box;
  }
  .authors {
    position: absolute;
    left: 0;
    right: 0;
    top: 30px;
    margin: 0;
    padding: 0;
    list-style: none;
    text-align: center;
    color: var(--ink);
    font-weight: 500;
    font-size: 54px;
    line-height: 60px;
    text-shadow:
      2px 0 0 var(--paper), -2px 0 0 var(--paper),
      0 2px 0 var(--paper), 0 -2px 0 var(--paper),
      2px 2px 0 var(--paper), -2px -2px 0 var(--paper),
      2px -2px 0 var(--paper), -2px 2px 0 var(--paper);
  }
</style>
</head>
<body>
  <main class="cover">
    <div class="cover-art" role="img" aria-label="Rows of receding digits washed in a spectrum of red, yellow, green and blue light"></div>

    <section class="title-plate">
      <h1 class="book-title">
        <span>Ledger Metrics</span>
        <span>for Leaders &amp;</span>
        <span>Finance Directors</span>
      </h1>
    </section>

    <section class="author-band">
      <ul class="authors">
        <li>Marcus Rend</li>
        <li>Alden J. Pavetta</li>
      </ul>
    </section>
  </main>
</body>
</html>
```